New Branding Business Card Design

Redesign business card according to new branding update.

** The design received so far are single color + BLACK.
I'd encourage designer to use different tones of blue / purple as described in the Designer Brief color palette

Target Market(s)

International

Industry/Entity Type

Medical Equipment

Contact Information for Business Card

Logo on one side (Designer can decide if they want to move certain info from the other side to save space)

Main body info (company name, individual name in both English and Chinese, contact info etc) on the other
Prefer a 'cleaner' layout - vs 'all over the place'
Prefer flush left alignment

Font styles to use
Sans Serif

Requirements
Must have
• Key info
• (Company name (English)): VORAM (HK) Limited
• (Name (English)): Marcus L. Pryde
• (Credential): FCPA, FHKSI
• (Title): Founder, Managing Director & CEO
• For the following info, designers decide whether to use colon or no colon, stroke separator, or use icon gfx for T (for telephone fixed line, M for mobile etc.)
• T: +852 3517 VORAM / +852 3517 4062
• M: +852 6243 7719 / + 86 139 2745 3186
• E: marcus.l.pryde@voram-example.hk
Nice to have
• Depending on the space and spacing available designers can add or use fuller title and other info
• Title: Chairman of the Executive Committee, Founder, Managing Director & CEO
• (Name (Chinese)): 林書恒
Should not have
• One of our business entities a long company name that cannot be broken into 2 lines
• makes vertical implementation almost impossible

```html
<!DOCTYPE html>
<html lang="en">
<head>
<meta charset="utf-8">
<title>VORAM (HK) Limited — Business Card</title>
<link rel="stylesheet" href="https://fonts.googleapis.com/css2?family=Montserrat:wght@400;500;600;700&display=swap">
<style>
  :root {
    --purple: #62399b;
    --purple-light: #a784d8;
    --grey: #8c8c8c;
    --grey-light: #d9d9de;
    --ink: #3a3a3a;
    --ink-soft: #6b6b6b;
    --paper: #ffffff;
    --backdrop: #f1f1f3;
  }
  html, body {
    margin: 0;
    padding: 0;
    width: 769px;
    height: 1200px;
    overflow: hidden;
    background: var(--backdrop);
    font-family: "Montserrat", Arial, sans-serif;
  }
  .sheet {
    width: 769px;
    height: 1200px;
    display: flex;
    flex-direction: column;
    align-items: center;
    justify-content: center;
    gap: 110px;
  }
  .card {
    position: relative;
    width: 620px;
    height: 354px;
    background: var(--paper);
    overflow: hidden;
    box-shadow: 10px 10px 0 rgba(0,0,0,0.12), 0 2px 6px rgba(0,0,0,0.08);
  }
  .card__corners {
    position: absolute;
    inset: 0;
    width: 100%;
    height: 100%;
  }
  /* Front */
  .front__brand {
    position: absolute;
    left: 0; right: 0;
    top: 122px;
    text-align: center;
  }
  .brand-name {
    display: inline-flex;
    align-items: center;
    gap: 12px;
    font-weight: 700;
    font-size: 46px;
    letter-spacing: 6px;
    color: var(--purple);
  }
  .brand-name__square {
    width: 30px;
    height: 30px;
    background: var(--purple);
    border-radius: 4px;
  }
  .front__email {
    margin-top: 16px;
    font-size: 19px;
    font-weight: 500;
    color: var(--ink);
  }
  /* Back */
  .back__company {
    position: absolute;
    left: 40px;
    top: 34px;
    display: flex;
    align-items: center;
    gap: 12px;
    font-size: 15px;
    font-weight: 600;
    color: var(--ink);
  }
  .back__company .brand-name__square {
    width: 26px;
    height: 26px;
  }
  .back__divider {
    position: absolute;
    left: 40px;
    top: 80px;
    width: 220px;
    height: 1px;
    background: var(--grey-light);
  }
  .person {
    position: absolute;
    left: 40px;
    top: 100px;
  }
  .person__name {
    margin: 0;
    font-size: 28px;
    font-weight: 700;
    color: var(--purple);
  }
  .person__title {
    margin: 4px 0 0;
    font-size: 11px;
    color: var(--ink-soft);
  }
  .contact {
    list-style: none;
    margin: 18px 0 0;
    padding: 0;
    font-size: 11.5px;
    color: var(--ink);
  }
  .contact__item {
    display: flex;
    align-items: flex-start;
    gap: 10px;
    margin-bottom: 9px;
    line-height: 1.35;
  }
  .contact__icon {
    flex: none;
    width: 18px;
    height: 18px;
  }
  .back__watermark {
    position: absolute;
    left: 360px;
    top: 130px;
    font-size: 52px;
    font-weight: 700;
    letter-spacing: 6px;
    color: #f0edf5;
  }
  .back__email {
    position: absolute;
    right: 110px;
    bottom: 26px;
    font-size: 10.5px;
    color: var(--ink);
  }
</style>
</head>
<body>
<main class="sheet">

  <section class="card card--front" aria-label="Business card, logo side">
    <svg class="card__corners" viewBox="0 0 620 354" aria-hidden="true">
      <g transform="translate(40,-40) rotate(-35)">
        <rect x="-60" y="-40" width="170" height="150" rx="26" fill="var(--grey)"/>
      </g>
      <g transform="translate(0,-30) rotate(-35)">
        <rect x="-120" y="-30" width="190" height="170" rx="26" fill="var(--purple)"/>
      </g>
      <line x1="118" y1="58" x2="30" y2="120" stroke="var(--purple-light)" stroke-width="6" stroke-linecap="round"/>
      <g transform="translate(590,400) rotate(-35)">
        <rect x="-100" y="-110" width="170" height="150" rx="26" fill="var(--grey)"/>
      </g>
      <g transform="translate(630,400) rotate(-35)">
        <rect x="-90" y="-120" width="190" height="170" rx="26" fill="var(--purple)"/>
      </g>
      <line x1="520" y1="270" x2="600" y2="214" stroke="var(--purple-light)" stroke-width="6" stroke-linecap="round"/>
    </svg>
    <div class="front__brand">
      <div class="brand-name"><span class="brand-name__square"></span>VORAM</div>
      <div class="front__email">hello@voram-example.hk</div>
    </div>
  </section>

  <section class="card card--back" aria-label="Business card, contact side">
    <svg class="card__corners" viewBox="0 0 620 354" aria-hidden="true">
      <g transform="translate(610,390) rotate(-35)">
        <rect x="-100" y="-110" width="170" height="150" rx="26" fill="var(--grey)"/>
      </g>
      <g transform="translate(650,400) rotate(-35)">
        <rect x="-90" y="-120" width="190" height="170" rx="26" fill="var(--purple)"/>
      </g>
      <line x1="540" y1="280" x2="612" y2="230" stroke="var(--purple-light)" stroke-width="6" stroke-linecap="round"/>
    </svg>

    <div class="back__company">
      <span class="brand-name__square"></span>VORAM (HK) Limited
    </div>
    <div class="back__divider"></div>
    <div class="back__watermark" aria-hidden="true">VORAM</div>

    <div class="person">
      <h1 class="person__name">Marcus L. Pryde</h1>
      <p class="person__title">Founder, Managing Director &amp; CEO</p>
      <ul class="contact">
        <li class="contact__item">
          <svg class="contact__icon" viewBox="0 0 18 18" aria-label="Telephone">
            <circle cx="9" cy="9" r="8" fill="none" stroke="var(--purple)" stroke-width="1.3"/>
            <path d="M6 5.5c.6-.5 1.1-.4 1.4.2l.5 1.1c.2.4 0 .8-.3 1l-.4.3c.4 1 1.2 1.8 2.2 2.2l.3-.4c.3-.3.7-.4 1-.3l1.1.5c.6.3.7.8.2 1.4-.8.9-1.9.9-3.4-.1-1.3-.9-2.2-1.8-2.9-3-.9-1.5-.6-2.4-.1-2.9z" fill="var(--purple)"/>
          </svg>
          <span>+852 3517 VORAM<br>+852 3517 4062</span>
        </li>
        <li class="contact__item">
          <svg class="contact__icon" viewBox="0 0 18 18" aria-label="Mobile">
            <circle cx="9" cy="9" r="8" fill="none" stroke="var(--purple)" stroke-width="1.3"/>
            <rect x="6.3" y="4.3" width="5.4" height="9.4" rx="1" fill="none" stroke="var(--purple)" stroke-width="1.2"/>
            <circle cx="9" cy="12" r="0.6" fill="var(--purple)"/>
          </svg>
          <span>+852 6243 7719<br>+ 86 139 2745 3186</span>
        </li>
        <li class="contact__item">
          <svg class="contact__icon" viewBox="0 0 18 18" aria-label="Email">
            <circle cx="9" cy="9" r="8" fill="none" stroke="var(--purple)" stroke-width="1.3"/>
            <rect x="4.6" y="5.8" width="8.8" height="6.4" rx="0.8" fill="none" stroke="var(--purple)" stroke-width="1.2"/>
            <path d="M4.8 6.2L9 9.4l4.2-3.2" fill="none" stroke="var(--purple)" stroke-width="1.2"/>
          </svg>
          <span>marcus.l.pryde@voram-example.hk</span>
        </li>
      </ul>
    </div>

    <div class="back__email">hello@voram-example.hk</div>
  </section>

</main>
</body>
</html>
```